New Toothpaste brand needs a logo & packaging design

Our company is launching a new toothpaste and is looking for a logo and packaging design. The toothpaste brand is called Brivana. The packaging should have the same design quality as the major international brands, such as Lumora, Lumora Totalcare, Dentiva, Pexolo, Wind-rise, Marvest, etc. The dominant colors for our brand should be hues of blue, similar to other major brands. In addition, there should be a little bit of green to represent the "Fresh Mint Blast" flavor and the "Extracts of Aloe Vera" included in the ingredients.

There are typically 3 unique sides on a toothpaste box:

The face: Repeated on ~3 sides of the 4 faces of the box
The back: The 4th box face has the instructions for use, ingredients, company information, bar code/product info, and some branding elements.
The sides: Usually consisting of just the logo, flavor etc.

Please refer to existing brands such as Lumora, Lumora Total-care, and Dentiva for an example of typical box layout and elements.

Task Details:
Package Dimensions: 180 mm x 48 mm x 28 mm, 100 ml toothpaste tube
Brand Name: Brivana
Description: Fluoride Toothpaste
Flavor: Fresh Mint Blast
5 Actions: Protects against cavities and tartar, freshens breath, whitens teeth, and maintains healthy gums. These actions can also be made into a list like Lumora Total Care or Dentiva Max care. For instance, Strong Teeth, Fresh Breath, Whitening, Healthy Gums, Cavity and Tartar Protection.
Also contains whitening micro particles and extracts of aloe vera which may be highlighted on the package

Overall, the look should be high quality and with the same look and feel as the big brands mentioned previously. We do not have an existing logo for this brand. The face of the package is the most important element as it is often repeated on several sides and on the tube itself.

Please let me know if you have any questions.

I've attached some of our favorite big brand designs below. I would say the Lumora Total Care and Gleam vers

The logos I've seen so far for Brivana, have been a bit too bold. A little bold is okay, but just needs to be moderate. 

I would like the colors to be bright and appealing. I mentioned shades of blue being the major color, but green should also be highlighted as well, perhaps in a 80% blue to 20% green ratio. 

Target Market(s)

adult consumer of toothpaste, both female and male.

Industry/Entity Type

It Company

Requirements
Must have
• A logo with the brand name: Brivana
Description or sub text: Fluoride Toothpaste
Flavor: Fresh Mint Blast
A phrase or list describing the Toothpaste Actions: e.g., Protects against cavities and tartar, freshens breath, whitens teeth, and maintains healthy gums. Or as a list simialr to Lumora Total Care or Dentiva Max Care:
-Anti-cavity
-Anti-tartar
-Fresh breath
-Whitening
-Healthy Gums

Special ingredient of "whitening micro particles: and "extracts of aloe vera", which should also be highlighted.

The color should mostly be shades of blue, with only a little bit of green to accentuate the fresh mint blast flavor and aloe vera

Nice to have
• The design should really look good next to lumora total care, gleam pure, and dentiva max care. These are our favorite designs.
Should not have
• For aloe vera, there is no need to show the plant.

The Brivana logo shouldn't be too Bold. This should be appeal to all consumers, not just men.

```html
<!DOCTYPE html>
<html lang="en">
<head>
<meta charset="utf-8">
<title>Brivana Fluoride Toothpaste – Carton Dieline</title>
<link href="https://fonts.googleapis.com/css2?family=Michroma&display=swap" rel="stylesheet">
<style>
  :root{
    --bg-light:#f4f5f7;
    --bg-dark:#c9ccd1;
    --navy:#0b3a78;
    --blue-deep:#0d4f97;
    --blue:#1670bf;
    --blue-bright:#1e9be0;
    --blue-pale:#5cc3f0;
    --green:#8cc63f;
    --silver:#e4e7ea;
    --silver-dark:#b9bfc6;
    --tag:#9aa3ad;
    --white:#ffffff;
  }
  html,body{margin:0;padding:0;overflow:hidden;}
  body{
    width:1200px;height:799px;
    background:radial-gradient(ellipse at 50% 40%,var(--bg-light) 0%,var(--bg-dark) 100%);
  }
  .artboard{display:block;width:1200px;height:799px;}
  .type{font-family:"Michroma",sans-serif;}
  .brand-name{fill:var(--white);}
  .descriptor{fill:var(--white);font-size:8.5px;}
  .descriptor-side{fill:var(--white);font-size:7.5px;}
  .flavor-tag-text{fill:var(--white);font-size:9px;letter-spacing:.3px;}
  .flavor-tag-text-side{fill:var(--white);font-size:7.6px;letter-spacing:.2px;}
  .benefit{fill:var(--navy);font-size:6.2px;}
  .claim{fill:var(--navy);font-size:6.2px;}
  .band-text{fill:var(--white);font-size:5.4px;}
  .wordmark-navy{fill:var(--navy);font-size:26px;}
  .wordmark-bright{fill:var(--blue-bright);font-size:26px;}
  .end-brand{fill:var(--white);}
  .end-brand-blue{fill:var(--blue);}
</style>
</head>
<body>
<svg class="artboard" viewBox="0 0 840 560" preserveAspectRatio="xMidYMid meet" xmlns="http://www.w3.org/2000/svg" aria-label="Brivana toothpaste carton dieline and wordmarks">
  <defs>
    <linearGradient id="blueField" x1="0" y1="0" x2="1" y2="0">
      <stop offset="0" stop-color="var(--blue-deep)"/>
      <stop offset=".55" stop-color="var(--blue)"/>
      <stop offset="1" stop-color="var(--blue-bright)"/>
    </linearGradient>
    <linearGradient id="silverField" x1="0" y1="0" x2="1" y2="1">
      <stop offset="0" stop-color="var(--white)"/>
      <stop offset=".5" stop-color="var(--silver)"/>
      <stop offset="1" stop-color="var(--silver-dark)"/>
    </linearGradient>
    <clipPath id="bodyClip"><rect x="60" y="5" width="425" height="315"/></clipPath>
  </defs>

  <g class="dieline" transform="translate(120,20)">

    <!-- left end tuck panel -->
    <g class="end-panel end-panel-left">
      <path d="M60 25 H20 Q4 25 4 41 V109 Q4 125 20 125 H60 Z" fill="url(#blueField)" stroke="var(--white)" stroke-width="2"/>
      <text class="type end-brand" font-size="15" transform="translate(24,36) rotate(90)">Brivana</text>
      <text class="type end-brand" font-size="4.6" transform="translate(14,38) rotate(90)">FLUORIDE TOOTHPASTE</text>
    </g>

    <!-- left bottom dust flap -->
    <path class="dust-flap" d="M110 328 H82 Q70 328 70 340 V386 Q70 398 82 398 H110 Z" fill="url(#blueField)"/>

    <!-- right end panel -->
    <g class="end-panel end-panel-right">
      <path d="M485 145 H588 Q604 145 604 161 V222 L592 228 H485 Z" fill="url(#silverField)"/>
      <path d="M485 228 H545 V320 H485 Z" fill="url(#silverField)"/>
      <text class="type end-brand-blue" font-size="11" transform="translate(520,238) rotate(90)">Brivana</text>
      <text class="type end-brand-blue" font-size="3.8" transform="translate(510,240) rotate(90)">FLUORIDE TOOTHPASTE</text>
    </g>

    <!-- main body: three faces -->
    <g class="carton-body" clip-path="url(#bodyClip)">
      <rect x="60" y="5" width="425" height="315" fill="url(#blueField)"/>
      <polygon class="silver-field" points="355,5 485,5 485,320 355,320 415,162" fill="url(#silverField)"/>
      <polygon class="green-chevron" points="310,5 335,5 395,162 335,320 310,320 370,162" fill="var(--green)"/>
      <polygon class="light-chevron" points="335,5 357,5 417,162 357,320 335,320 395,162" fill="var(--blue-pale)"/>
      <polygon class="silver-wedge" points="330,182 395,140 485,140 485,225 395,225" fill="url(#silverField)"/>
      <line x1="60" y1="140" x2="485" y2="140" stroke="var(--white)" stroke-opacity=".35" stroke-width=".6"/>
      <line x1="60" y1="225" x2="485" y2="225" stroke="var(--white)" stroke-opacity=".35" stroke-width=".6"/>
    </g>

    <!-- face 1 -->
    <g class="face face-front">
      <rect class="flavor-tag" x="128" y="47" width="158" height="14" fill="var(--tag)"/>
      <text class="type flavor-tag-text" x="132" y="57.5">FRESH MINT BLAST</text>
      <text class="type brand-name" x="150" y="100" font-size="30" textLength="168" lengthAdjust="spacingAndGlyphs">Brivana</text>
      <text class="type descriptor" x="330" y="116" text-anchor="end">FLUORIDE TOOTHPASTE</text>
      <g class="badge badge-care">
        <circle cx="444" cy="55" r="14" fill="var(--white)" stroke="var(--blue)" stroke-width="2.5"/>
        <path d="M444 46 V64 M437 55 H451" stroke="var(--blue)" stroke-width="3" stroke-linecap="round"/>
      </g>
      <g class="benefit-list">
        <text class="type benefit" x="380" y="80">· ANTI-CAVITY</text>
        <text class="type benefit" x="386" y="93">· ANTI-TARTAR</text>
        <text class="type benefit" x="392" y="106">· FRESH BREATH</text>
        <text class="type benefit" x="398" y="119">· WHITENING</text>
        <text class="type benefit" x="404" y="132">· HEALTHY GUMS</text>
      </g>
    </g>

    <!-- face 2 (narrow side) -->
    <g class="face face-side">
      <rect class="flavor-tag" x="128" y="149" width="130" height="12" fill="var(--tag)"/>
      <text class="type flavor-tag-text-side" x="132" y="158">FRESH MINT BLAST</text>
      <text class="type brand-name" x="148" y="192" font-size="25" textLength="142" lengthAdjust="spacingAndGlyphs">Brivana</text>
      <text class="type descriptor-side" x="292" y="206" text-anchor="end">FLUORIDE TOOTHPASTE</text>
      <text class="type claim" x="414" y="160">DEVELOPED</text>
      <text class="type claim" x="414" y="169">WITH DENTAL</text>
      <text class="type claim" x="414" y="178">EXPERTS</text>
      <rect class="protection-band" x="345" y="186" width="140" height="14" fill="var(--navy)"/>
      <text class="type band-text" x="382" y="195" textLength="98" lengthAdjust="spacingAndGlyphs">ALL-AROUND PROTECTION</text>
      <g class="badge badge-tooth">
        <circle cx="358" cy="182" r="20" fill="var(--navy)" stroke="var(--white)" stroke-width="2.5"/>
        <path d="M349 174 Q352 169 358 172 Q364 169 367 174 Q369 181 365 186 L363 193 Q361 195 360 191 L358 185 L356 191 Q355 195 353 193 L351 186 Q347 181 349 174 Z" fill="var(--white)"/>
      </g>
    </g>

    <!-- face 3 -->
    <g class="face face-rear">
      <rect class="flavor-tag" x="128" y="237" width="158" height="14" fill="var(--tag)"/>
      <text class="type flavor-tag-text" x="132" y="247.5">FRESH MINT BLAST</text>
      <text class="type brand-name" x="150" y="288" font-size="30" textLength="168" lengthAdjust="spacingAndGlyphs">Brivana</text>
      <text class="type descriptor" x="330" y="304" text-anchor="end">FLUORIDE TOOTHPASTE</text>
      <g class="badge badge-care">
        <circle cx="444" cy="244" r="13" fill="var(--white)" stroke="var(--blue)" stroke-width="2.5"/>
        <path d="M444 236 V252 M436 244 H452" stroke="var(--blue)" stroke-width="3" stroke-linecap="round"/>
      </g>
      <g class="benefit-list">
        <text class="type benefit" x="410" y="268">· ANTI CAVITY</text>
        <text class="type benefit" x="405" y="279">· ANTI TARTAR</text>
        <text class="type benefit" x="405" y="290">· FRESH BREATH</text>
        <text class="type benefit" x="398" y="301">· WHITENING</text>
        <text class="type benefit" x="404" y="312">· HEALTHY GUMS</text>
      </g>
    </g>

    <!-- back panel -->
    <g class="face face-back">
      <rect x="110" y="320" width="375" height="85" fill="url(#blueField)"/>
      <polygon points="300,320 330,320 350,405 320,405" fill="var(--blue-pale)" opacity=".6"/>
      <rect class="info-box" x="140" y="336" width="343" height="64" rx="7" fill="var(--white)"/>
      <line x1="402" y1="342" x2="402" y2="394" stroke="var(--blue)" stroke-width=".8"/>
      <text class="type end-brand" font-size="9" transform="translate(126,338) rotate(90)">Brivana</text>
      <text class="type end-brand" font-size="3" transform="translate(119,338) rotate(90)">FLUORIDE TOOTHPASTE</text>
    </g>
  </g>

  <!-- wordmark versions -->
  <g class="wordmarks">
    <text class="type wordmark-navy" x="230" y="540">Brivana</text>
    <text class="type wordmark-bright" x="420" y="540">Brivana</text>
  </g>
</svg>
</body>
</html>
```